Events & Entertainment Production Coordination Business Cards

We need a business card for a new company based in Los Angeles called "Bright Harbor Works"
Our company brings people together for events and helps coordinate different productions. We bring artists from a different country to perform or do events in the U.S.
We are looking for something fun, lively, colorful, creative, and simple.
Nothing that looks too crisp, dark, stiff, or modern.
We connect people from different parts of the world, so definitely something eye-catching will be great!
Colors we would like to see are Black, Yellow, Red, White, Brown to name a few. (Feel free to use more!)
(Double-sided is an option also)
Business
Contact Information for Business Card
Contact Information to put on Business Card:
Name
Title
Address - 2 lines
Phone - place for 3 numbers
E-mail
URL

```html
<!DOCTYPE html>
<html lang="en">
<head>
<meta charset="utf-8">
<title>Bright Harbor Works – Business Card</title>
<link rel="stylesheet" href="https://fonts.googleapis.com/css2?family=Lato:wght@400;700&display=swap">
<style>
  :root {
    --bg: #2c2c2e;
    --card: #fbfbfb;
    --red: #b3121c;
    --ink: #2e2e2e;
    --map: #f1dcdc;
    --map-soft: #f7ecec;
  }
  * { margin: 0; padding: 0; box-sizing: border-box; }
  html, body {
    width: 1200px; height: 997px; overflow: hidden;
    background: var(--bg);
    font-family: "Lato", Arial, sans-serif;
  }
  .stage {
    width: 1200px; height: 997px;
    display: flex; flex-direction: column; align-items: center; justify-content: center;
    gap: 56px;
  }
  .card {
    position: relative;
    width: 700px; height: 400px;
    background: var(--card);
    box-shadow: 0 10px 30px rgba(0,0,0,.45);
    overflow: hidden;
  }
  .world-map {
    position: absolute;
    background: radial-gradient(ellipse at 45% 50%, var(--map) 0%, var(--map-soft) 55%, rgba(247,236,236,0) 80%);
  }
  .card--front .world-map { left: 120px; top: 70px; width: 470px; height: 270px; }
  .card--back .world-map { left: 110px; top: 30px; width: 520px; height: 300px; }

  .brand {
    position: absolute; display: flex; align-items: center; gap: 14px;
    color: var(--red); font-weight: 700; letter-spacing: .5px;
    white-space: nowrap;
  }
  .brand__mark { width: 22px; height: 22px; background: var(--red); }
  .card--front .brand { left: 50%; top: 50%; transform: translate(-50%, -50%); font-size: 44px; }
  .card--front .brand__mark { width: 30px; height: 30px; }
  .card--back .brand { left: 50%; top: 36px; transform: translateX(-50%); font-size: 32px; }

  .holder {
    position: absolute; right: 400px; top: 178px; text-align: right;
  }
  .holder__name { color: var(--red); font-weight: 700; font-size: 24px; }
  .holder__title { color: var(--ink); font-size: 17px; margin-top: 4px; }
  .holder__address { color: var(--red); font-weight: 700; font-size: 19px; line-height: 1.35; margin-top: 30px; }

  .divider {
    position: absolute; left: 318px; top: 170px; width: 3px; height: 130px;
    background: linear-gradient(to bottom, rgba(179,18,28,0), var(--red) 45%, rgba(179,18,28,0));
  }
  .contacts {
    position: absolute; left: 345px; top: 150px; list-style: none;
  }
  .contacts li {
    display: flex; align-items: center; gap: 12px;
    color: var(--ink); font-size: 17px; line-height: 1; margin-bottom: 13px;
  }
  .contacts svg { width: 17px; height: 17px; fill: var(--red); flex: none; }
</style>
</head>
<body>
<main class="stage">

  <section class="card card--front" aria-label="Card front">
    <div class="world-map" role="img" aria-label="Faint dotted world map in soft red"></div>
    <div class="brand"><span class="brand__mark"></span><span>Bright Harbor Works</span></div>
  </section>

  <section class="card card--back" aria-label="Card back">
    <div class="world-map" role="img" aria-label="Faint dotted world map in soft red"></div>
    <div class="brand"><span class="brand__mark"></span><span>Bright Harbor Works</span></div>

    <div class="holder">
      <p class="holder__name">Daniel Ferris</p>
      <p class="holder__title">Chief Operating Officer</p>
      <p class="holder__address">48 Linden Avenue,<br>Fairview, PA 15230</p>
    </div>

    <div class="divider"></div>

    <ul class="contacts">
      <li>
        <svg viewBox="0 0 24 24"><path d="M6.6 10.8a15 15 0 0 0 6.6 6.6l2.2-2.2c.3-.3.7-.4 1-.2 1.1.4 2.3.6 3.6.6.6 0 1 .4 1 1V20c0 .6-.4 1-1 1A17 17 0 0 1 3 4c0-.6.4-1 1-1h3.5c.6 0 1 .4 1 1 0 1.3.2 2.5.6 3.6.1.3 0 .7-.2 1z"/></svg>
        <span>555-214-7120</span>
      </li>
      <li>
        <svg viewBox="0 0 24 24"><path d="M6 2h12v5H6z"/><path d="M3 8h18a1 1 0 0 1 1 1v8h-4v-3H6v3H2V9a1 1 0 0 1 1-1z"/><path d="M7 15h10v7H7z"/></svg>
        <span>555-214-7122</span>
      </li>
      <li>
        <svg viewBox="0 0 24 24"><path d="M2 5h20v14H2z" fill="none"/><path d="M2 5h20v2l-10 6L2 7z"/><path d="M2 9l10 6 10-6v10H2z"/></svg>
        <span>dan@brightharborworks.com</span>
      </li>
      <li>
        <svg viewBox="0 0 24 24"><path d="M10.6 13.4a1 1 0 0 1 0-1.4l3-3a1 1 0 1 1 1.4 1.4l-3 3a1 1 0 0 1-1.4 0z"/><path d="M13 6.3l1.8-1.8a4 4 0 0 1 5.7 5.7L18.7 12l-1.4-1.4 1.8-1.8a2 2 0 0 0-2.9-2.9l-1.8 1.8zM11 17.7l-1.8 1.8a4 4 0 0 1-5.7-5.7L5.3 12l1.4 1.4-1.8 1.8a2 2 0 0 0 2.9 2.9l1.8-1.8z"/></svg>
        <span>www.brightharborworks.com</span>
      </li>
    </ul>
  </section>

</main>
</body>
</html>
```